NEW FACEBOOK AD CREATIVES FOR MARKETING AGENCY

We need one single static image AND a Carousel Ad Design With 5 Cards Total in it.

We advertise a SaaS Product that teaches businesses how to use incentive based marketing to get more sales and leads.

Using our service businesses can give away smart devices like smartwatches, earpods, mp4 players, tablets, etc. as a gift bonus along with their product or service as an added value benefit to help them create more attractive offers and to get more sales.

I have attached two designs that get me my best results on facebook ads so far so I want to create something very similar with a different look and showcasing 3-4 of the items I have attached images for.

CONTENT & INSTRUCTIONS:
MAIN TEXT: TRIPLE YOUR SALES OFFERING FREE SMART DEVICES AS A BONUS FOR BUYING YOUR PRODUCT OR SERVICE

Target Market(s)

ENTREPRENEURS, INVESTORS, BUSINESS OWNERS, MEDIA AGENCIES, BROKERAGES

Industry/Entity Type

marketing gifting

Requirements
Must have
• must match color scheme of website www.brightlooprewardhub.biz as this is where they will be redirected to when they click.
Nice to have
• the ads must be 1080x1080 Static newsfeed ad and carousel ads

```html
<!DOCTYPE html>
<html lang="en">
<head>
<meta charset="utf-8">
<title>Brightloop Reward Hub – Carousel Ad Set</title>
<link rel="stylesheet" href="https://fonts.googleapis.com/css2?family=Montserrat:ital,wght@0,600;0,700;0,800;1,900&display=swap">
<style>
  :root{
    --canvas:#2a2a2a;
    --blue-light:#4fb0ff;
    --blue:#0d63d6;
    --blue-deep:#06378c;
    --navy:#0b2a6b;
    --orange:#f39200;
    --white:#ffffff;
    --device-dark:#1b1d22;
    --device-mid:#3a3d45;
    --bud-light:#f4f6f9;
    --bud-shade:#c9d0da;
  }
  *{box-sizing:border-box;margin:0;padding:0}
  html,body{width:849px;height:1200px;overflow:hidden;background:var(--canvas)}
  body{position:relative;font-family:"Montserrat",Arial,sans-serif}

  .ad-card{
    position:absolute;width:370px;height:370px;overflow:hidden;
    background:radial-gradient(circle at 55% 32%,var(--blue-light) 0%,var(--blue) 45%,var(--blue-deep) 100%);
  }
  .card-1{left:26px;top:26px}
  .card-2{left:26px;top:418px}
  .card-3{left:26px;top:810px}
  .card-4{left:440px;top:240px}
  .card-5{left:440px;top:628px}

  .brand{position:absolute;left:14px;top:14px;display:flex;align-items:center;gap:6px;z-index:3}
  .brand-dot{width:14px;height:14px;border-radius:50%;background:var(--white)}
  .brand-name{font-weight:800;font-size:13px;color:var(--white);line-height:1.05;width:90px}

  .device{position:absolute;z-index:1}
  .device-dark{background:linear-gradient(160deg,var(--device-mid),var(--device-dark) 70%)}
  .device-bud{background:linear-gradient(160deg,var(--bud-light),var(--bud-shade))}
  .speaker{border-radius:60px}
  .watch{border-radius:22px}
  .headphones{border-radius:50%}
  .earbuds{border-radius:14px}

  .info-panel{position:absolute;left:0;bottom:0;width:100%;height:140px;z-index:2}
  .info-panel svg{position:absolute;left:0;top:0}
  .offer{position:absolute;left:16px;bottom:22px;width:200px;z-index:3}
  .offer-kicker{color:var(--orange);font-weight:800;font-size:13px;letter-spacing:.3px}
  .offer-text{color:var(--navy);font-weight:700;font-size:11.5px;line-height:1.28;margin-top:2px;text-transform:uppercase}
  .offer-button{display:inline-block;margin-top:9px;background:var(--orange);color:var(--white);
    font-weight:700;font-size:8px;line-height:1.15;padding:5px 10px;border-radius:3px;width:92px}

  .badge{position:absolute;right:10px;bottom:28px;width:150px;height:150px;z-index:4}
  .badge svg{position:absolute;inset:0}
  .badge-text{position:absolute;inset:0;display:flex;flex-direction:column;justify-content:center;align-items:center;
    color:var(--white);font-weight:900;font-style:italic;font-size:25px;line-height:.98;text-align:center;transform:rotate(-8deg)}
</style>
</head>
<body>

<svg width="0" height="0" style="position:absolute" aria-hidden="true">
  <defs>
    <radialGradient id="badgeFill" cx="50%" cy="40%" r="60%">
      <stop offset="0" stop-color="#2f8bff"/>
      <stop offset="1" stop-color="#0a3f9e"/>
    </radialGradient>
    <polygon id="starburst" fill="url(#badgeFill)" stroke="#ffffff" stroke-width="3"
      points="138,70 126.9,81.3 132.8,96 118.2,102.2 118.1,118.1 102.2,118.2 96,132.8 81.3,126.9 70,138 58.7,126.9 44,132.8 37.8,118.2 21.9,118.1 21.8,102.2 7.2,96 13.1,81.3 2,70 13.1,58.7 7.2,44 21.8,37.8 21.9,21.9 37.8,21.8 44,7.2 58.7,13.1 70,2 81.3,13.1 96,7.2 102.2,21.8 118.1,21.9 118.2,37.8 132.8,44 126.9,58.7"/>
    <path id="panelShape" d="M0 40 Q120 0 370 18 L370 140 L0 140 Z" fill="#ffffff"/>
  </defs>
</svg>

<!-- Card 1: speaker + watch -->
<section class="ad-card card-1">
  <div class="brand"><span class="brand-dot"></span><span class="brand-name">Brightloop Reward Hub</span></div>
  <div class="device device-dark speaker" style="left:120px;top:30px;width:230px;height:110px" role="img" aria-label="Black portable Bluetooth speaker"></div>
  <div class="device device-dark watch" style="left:55px;top:95px;width:100px;height:125px" role="img" aria-label="Black smartwatch with square display"></div>
  <div class="info-panel"><svg width="370" height="140"><use href="#panelShape"/></svg></div>
  <div class="offer">
    <p class="offer-kicker">OFFERING</p>
    <p class="offer-text">Free smart devices as a bonus for buying your product or service</p>
    <span class="offer-button">Get a Free Sample Package</span>
  </div>
  <div class="badge"><svg viewBox="0 0 140 140" width="150" height="150"><use href="#starburst"/></svg><p class="badge-text">TRIPLE<br>YOUR<br>SALES</p></div>
</section>

<!-- Card 2: headphones + earbuds -->
<section class="ad-card card-2">
  <div class="brand"><span class="brand-dot"></span><span class="brand-name">Brightloop Reward Hub</span></div>
  <div class="device device-dark headphones" style="left:150px;top:20px;width:190px;height:190px" role="img" aria-label="Black over-ear wireless headphones"></div>
  <div class="device device-bud earbuds" style="left:50px;top:140px;width:80px;height:90px" role="img" aria-label="White wireless earbuds with charging case"></div>
  <div class="info-panel"><svg width="370" height="140"><use href="#panelShape"/></svg></div>
  <div class="offer">
    <p class="offer-kicker">OFFERING</p>
    <p class="offer-text">Free smart devices as a bonus for buying your product or service</p>
    <span class="offer-button">Get a Free Sample Package</span>
  </div>
  <div class="badge"><svg viewBox="0 0 140 140" width="150" height="150"><use href="#starburst"/></svg><p class="badge-text">TRIPLE<br>YOUR<br>SALES</p></div>
</section>

<!-- Card 3: watch + earbuds -->
<section class="ad-card card-3">
  <div class="brand"><span class="brand-dot"></span><span class="brand-name">Brightloop Reward Hub</span></div>
  <div class="device device-dark watch" style="left:160px;top:15px;width:150px;height:210px;border-radius:70px" role="img" aria-label="Round black smartwatch with digital time display"></div>
  <div class="device device-bud earbuds" style="left:40px;top:140px;width:90px;height:95px" role="img" aria-label="White wireless earbuds with charging case"></div>
  <div class="info-panel"><svg width="370" height="140"><use href="#panelShape"/></svg></div>
  <div class="offer">
    <p class="offer-kicker">OFFERING</p>
    <p class="offer-text">Free smart devices as a bonus for buying your product or service</p>
    <span class="offer-button">Get a Free Sample Package</span>
  </div>
  <div class="badge"><svg viewBox="0 0 140 140" width="150" height="150"><use href="#starburst"/></svg><p class="badge-text">TRIPLE<br>YOUR<br>SALES</p></div>
</section>

<!-- Card 4: earbuds + watch -->
<section class="ad-card card-4">
  <div class="brand"><span class="brand-dot"></span><span class="brand-name">Brightloop Reward Hub</span></div>
  <div class="device device-dark watch" style="left:190px;top:25px;width:120px;height:170px" role="img" aria-label="Black smartwatch with square display"></div>
  <div class="device device-bud earbuds" style="left:80px;top:100px;width:90px;height:110px" role="img" aria-label="White wireless earbuds with open charging case"></div>
  <div class="info-panel"><svg width="370" height="140"><use href="#panelShape"/></svg></div>
  <div class="offer">
    <p class="offer-kicker">OFFERING</p>
    <p class="offer-text">Free smart devices as a bonus for buying your product or service</p>
    <span class="offer-button">Get a Free Sample Package</span>
  </div>
  <div class="badge"><svg viewBox="0 0 140 140" width="150" height="150"><use href="#starburst"/></svg><p class="badge-text">TRIPLE<br>YOUR<br>SALES</p></div>
</section>

<!-- Card 5: speaker + earbuds -->
<section class="ad-card card-5">
  <div class="brand"><span class="brand-dot"></span><span class="brand-name">Brightloop Reward Hub</span></div>
  <div class="device device-dark speaker" style="left:110px;top:25px;width:245px;height:115px" role="img" aria-label="Black portable Bluetooth speaker"></div>
  <div class="device device-bud earbuds" style="left:90px;top:115px;width:95px;height:105px" role="img" aria-label="White wireless earbuds with open charging case"></div>
  <div class="info-panel"><svg width="370" height="140"><use href="#panelShape"/></svg></div>
  <div class="offer">
    <p class="offer-kicker">OFFERING</p>
    <p class="offer-text">Free smart devices as a bonus for buying your product or service</p>
    <span class="offer-button">Get a Free Sample Package</span>
  </div>
  <div class="badge"><svg viewBox="0 0 140 140" width="150" height="150"><use href="#starburst"/></svg><p class="badge-text">TRIPLE<br>YOUR<br>SALES</p></div>
</section>

</body>
</html>
```